integrative health clinic-Medical massage, acupuncture, chiropractic

we like our logo, but are open to new ideas. We need a new card design. We have added chiropractic and acupuncture that we have put under the name of the business. We are an integrative medical clinic

Target Market(s)

General public, athletes

Contact Information for Business Card

Phone 5055582917
Fax 5055582916
Hours Monday-Friday 9-6
Saturday 10-6
The 20% can be smaller on the back

Colors
3176b5
0355a3

Requirements
Must have
• Logo but am open to ideas
Nice to have
• We are an integrated medical clinic but also want to be personable. We want the card fun and inviting

```html
<!DOCTYPE html>
<html lang="en">
<head>
<meta charset="utf-8">
<title>Open Motion Wellness – Business Card</title>
<link rel="stylesheet" href="https://fonts.googleapis.com/css2?family=Lato:wght@400;700&family=Roboto:wght@400&family=Roboto+Condensed:wght@400&display=swap">
<style>
  :root {
    --brand-blue: #2a3f9b;
    --ink: #111111;
    --paper: #ffffff;
    --backdrop: #d9d9d9;
    --body-font: "Lato", sans-serif;
    --name-font: "Roboto Condensed", sans-serif;
    --offer-font: "Roboto", sans-serif;
  }
  * { margin: 0; padding: 0; box-sizing: border-box; }
  html, body { width: 1200px; height: 802px; overflow: hidden; }
  body { background: var(--backdrop); font-family: var(--body-font); position: relative; }

  .card {
    position: absolute;
    top: 238px;
    width: 545px;
    height: 326px;
    overflow: hidden;
  }
  .card--front { left: 35px; background: var(--paper); }
  .card--back { left: 620px; background: var(--brand-blue); color: var(--paper); text-align: center; }

  /* front */
  .front-shape { position: absolute; inset: 0; }
  .contact { position: absolute; left: 31px; top: 0; color: var(--paper); font-size: 13.5px; line-height: 19.5px; }
  .contact__row { position: absolute; left: 0; white-space: nowrap; display: flex; align-items: flex-start; gap: 6px; }
  .contact__row svg { flex: none; margin-top: 3px; }
  .contact__block { position: absolute; left: 0; white-space: nowrap; }

  .brand-vertical {
    position: absolute;
    left: 285px; top: 130px;
    width: 280px; height: 75px;
    transform: rotate(-90deg);
    transform-origin: center;
  }
  .brand-vertical__name { font-family: var(--name-font); font-size: 33px; font-weight: 400; color: var(--ink); line-height: 36px; white-space: nowrap; }
  .brand-vertical__row { display: flex; align-items: center; gap: 6px; margin-top: 1px; }
  .brand-vertical__mark { width: 16px; height: 16px; border-radius: 50%; background: var(--brand-blue); flex: none; }
  .brand-vertical__tag { font-size: 13px; color: var(--ink); white-space: nowrap; line-height: 16px; }
  .brand-vertical__services { font-size: 7.5px; font-weight: 700; letter-spacing: 0.6px; color: var(--brand-blue); margin-left: 22px; line-height: 12px; white-space: nowrap; }

  /* back */
  .book-label { position: absolute; top: 41px; width: 100%; font-size: 15px; }
  .book-url { position: absolute; top: 62px; width: 100%; font-size: 21px; }
  .brand-lockup { position: absolute; top: 120px; left: 0; width: 100%; }
  .brand-lockup__name { font-family: var(--name-font); font-size: 36px; font-weight: 400; line-height: 40px; }
  .brand-lockup__row { display: flex; justify-content: center; align-items: center; gap: 8px; margin-top: 1px; }
  .brand-lockup__mark { width: 20px; height: 20px; border-radius: 50%; background: var(--paper); }
  .brand-lockup__tag { font-size: 15px; }
  .brand-lockup__services { font-size: 8px; font-weight: 700; letter-spacing: 0.7px; margin-top: 1px; }
  .offer-band { position: absolute; top: 229px; left: 0; width: 100%; height: 41px; background: var(--paper); color: var(--brand-blue); font-family: var(--offer-font); font-size: 18px; line-height: 41px; }
  .coverage-note { position: absolute; top: 285px; width: 100%; font-size: 14.5px; }
</style>
</head>
<body>

<section class="card card--front" aria-label="Card front">
  <svg class="front-shape" viewBox="0 0 545 326" width="545" height="326" aria-hidden="true">
    <path d="M0 0 H120 C300 10 345 95 320 200 C305 260 270 300 232 326 H0 Z" fill="var(--brand-blue)"/>
    <path d="M130 0 C318 12 356 100 330 205 C315 265 278 305 248 326 H236 C275 300 312 260 325 200 C348 100 310 14 122 0 Z" fill="var(--brand-blue)"/>
  </svg>

  <div class="contact">
    <div class="contact__row" style="top:52px;">
      <svg width="11" height="14" viewBox="0 0 11 14"><path d="M5.5 0 A5.5 5.5 0 0 1 11 5.5 C11 9 5.5 14 5.5 14 C5.5 14 0 9 0 5.5 A5.5 5.5 0 0 1 5.5 0 Z" fill="#fff"/><circle cx="5.5" cy="5.3" r="2" fill="var(--brand-blue)"/></svg>
      <span>418 Alder Row, Suite 3<br>Clearwater, NM 87599</span>
    </div>
    <div class="contact__row" style="top:103px;">
      <svg width="14" height="11" viewBox="0 0 14 11"><path d="M1 4 C1 1 13 1 13 4 L10 4 L10 2.5 L4 2.5 L4 4 Z" fill="#fff"/><rect x="2" y="5" width="10" height="6" rx="1" fill="#fff"/></svg>
      <span>5055582917</span>
    </div>
    <div class="contact__row" style="top:122px;">
      <svg width="14" height="12" viewBox="0 0 14 12"><rect x="3" y="0" width="8" height="4" fill="#fff"/><rect x="0" y="4" width="14" height="5" rx="1" fill="#fff"/><rect x="3" y="8" width="8" height="4" fill="#fff"/></svg>
      <span>5055582916</span>
    </div>
    <div class="contact__row" style="top:144px;">
      <svg width="12" height="10" viewBox="0 0 12 10"><rect x="0.5" y="0.5" width="11" height="9" fill="none" stroke="#fff"/><path d="M0.5 0.5 L6 5.5 L11.5 0.5" fill="none" stroke="#fff"/></svg>
      <span>hello@openmotionwellness.com</span>
    </div>
    <div class="contact__block" style="top:172px;">Specializing in Medical<br>Sports Massage and<br>Manual Therapies</div>
    <div class="contact__block" style="top:237px;">HOURS<br>Monday-Friday 9 am-6 pm<br>Saturday 10 am-6 pm</div>
  </div>

  <div class="brand-vertical">
    <div class="brand-vertical__name">Open Motion Wellness</div>
    <div class="brand-vertical__row">
      <span class="brand-vertical__mark"></span>
      <span class="brand-vertical__tag">Sports Therapy and Wellness Center</span>
    </div>
    <div class="brand-vertical__services">CHIROPRACTIC AND ACUPUNCTURE</div>
  </div>
</section>

<section class="card card--back" aria-label="Card back">
  <div class="book-label">Book Online</div>
  <div class="book-url">www.openmotionwellness.com</div>
  <div class="brand-lockup">
    <div class="brand-lockup__name">Open Motion Wellness</div>
    <div class="brand-lockup__row">
      <span class="brand-lockup__mark"></span>
      <span class="brand-lockup__tag">Sports Therapy and Wellness Center</span>
    </div>
    <div class="brand-lockup__services">CHIROPRACTIC AND ACUPUNCTURE</div>
  </div>
  <div class="offer-band">20% OFF FIRST VISIT</div>
  <div class="coverage-note">We Accept some insurances, Worker's Comp and Personal Injury</div>
</section>

</body>
</html>
```